Webdesign für Personalvermittlung
Zielgruppe
Personalvermittlung
Aufgabenstellung
es soll einladend - nicht zu überladen und natürlich cool und modern sein

```html
<!DOCTYPE html>
<html lang="de">
<head>
<meta charset="utf-8">
<title>Klarweg Job – Wir über uns</title>
<link href="https://fonts.googleapis.com/css2?family=Manrope:wght@400;500;600;700;800&display=swap" rel="stylesheet">
<style>
:root{
  --green:#67bb46;
  --green-dark:#3f8a2f;
  --ink:#3b3b3b;
  --text:#555;
  --blue:#29a7df;
  --footer:#f6f6f8;
  --white:#fff;
}
*{margin:0;padding:0;box-sizing:border-box}
html,body{width:794px;height:1200px;overflow:hidden;background:var(--white)}
body{font-family:"Manrope",sans-serif;color:var(--ink)}
.page{position:relative;width:1366px;height:2064px;transform:scale(0.58126);transform-origin:0 0}
.page > *{position:absolute}
.bg-shapes{left:0;top:0;width:1366px;height:2064px}
.brand{display:flex;align-items:center;gap:10px;font-weight:800;font-size:17px;color:var(--ink);letter-spacing:.5px}
.brand-mark{width:34px;height:34px;background:var(--green);border-radius:4px}
.nav{display:flex;gap:46px;font-weight:600;font-size:18px}
.nav a{text-decoration:none;color:var(--white)}
.nav a.current{color:var(--green-dark)}
.hero-title{left:140px;top:148px;font-size:50px;line-height:60px;font-weight:800;text-transform:uppercase;color:var(--ink)}
.accent{color:var(--green)}
.hero-text{left:140px;top:408px;width:445px;font-size:23px;line-height:32px;font-weight:500;color:var(--ink)}
.photo{border-radius:9px}
.photo-hands{left:698px;top:139px;width:528px;height:435px;background:linear-gradient(135deg,#b8b4b0,#8d7a6c 45%,#6c6a72 80%,#9a9aa2)}
.intro-lead{left:140px;top:674px;width:440px;font-size:28px;line-height:50px;font-weight:600;color:var(--ink)}
.benefits{left:604px;top:678px;width:622px;list-style:none}
.benefits li{display:flex;gap:36px;font-size:17px;line-height:32px;color:var(--text);margin-bottom:32px}
.benefits svg{flex:none;margin-top:4px}
.photo-team{left:140px;top:1210px;width:528px;height:528px;background:linear-gradient(180deg,#f1f3f4 0%,#dfe3e4 35%,#8d8177 65%,#4f5a6a 100%)}
.kicker{left:700px;top:1212px;font-size:25px;color:var(--green);font-weight:500}
.contact-title{left:698px;top:1244px;width:520px;font-size:43px;line-height:46px;font-weight:800;text-transform:uppercase;color:var(--ink)}
.field{background:var(--white);border-radius:17px;height:34px;font-size:18px;color:#b5b5b5;padding:0 16px;display:flex;align-items:center;justify-content:space-between}
.field.filled{color:var(--ink)}
.f-first{left:698px;top:1387px;width:249px}
.f-last{left:977px;top:1387px;width:249px}
.f-mail{left:698px;top:1440px;width:528px}
.f-call{left:698px;top:1498px;width:249px}
.f-cv{left:977px;top:1498px;width:249px}
.f-msg{left:698px;top:1556px;width:528px;height:193px;border-radius:16px;align-items:flex-start;padding-top:4px}
.send{left:698px;top:1772px;width:173px;height:35px;border-radius:18px;background:var(--blue);color:var(--white);font-size:18px;font-weight:500;display:flex;align-items:center;justify-content:space-between;padding:0 20px 0 22px}
.footer{left:0;top:1922px;width:1366px;height:142px;background:var(--footer)}
.footer .brand{position:absolute;left:142px;top:28px}
.footer-nav{position:absolute;right:140px;top:12px;display:flex;gap:46px;font-size:18px;font-weight:500}
.footer-nav a{color:var(--ink);text-decoration:none}
.social{position:absolute;right:140px;top:54px;display:flex;gap:22px}
.social span{width:20px;height:20px;border-radius:50%;background:#5b6470}
.footer-rule{position:absolute;left:140px;top:99px;width:1086px;height:1px;background:#333}
.copyright{position:absolute;left:140px;top:113px;font-size:16px;color:#555}
.legal{position:absolute;right:140px;top:113px;display:flex;gap:32px;font-size:16px;color:#555}
</style>
</head>
<body>
<div class="page">
  <svg class="bg-shapes" viewBox="0 0 1366 2064" aria-hidden="true">
    <polygon points="635,0 1366,0 1366,540 1226,540 1226,139 708,139" fill="#67bb46"/>
    <polygon points="668,1360 1366,1360 1366,1822 430,1822 385,1738 668,1738" fill="#67bb46"/>
  </svg>

  <div class="brand" style="left:142px;top:30px"><span class="brand-mark"></span>KLARWEG JOB</div>
  <nav class="nav" style="right:140px;top:44px">
    <a href="#">Home</a><a href="#">Bewerber über uns</a><a href="#" class="current">Wir über uns</a>
  </nav>

  <h1 class="hero-title">Unser <span class="accent">Team</span> steht<br>dir als<br><span class="accent">vertrauensvoller</span><br>Partner zur Seite</h1>
  <p class="hero-text">In einer Welt voller Herausforderungen und Möglichkeiten ist es entscheidend, einen Partner an seiner Seite zu haben, dem man vertrauen kann.</p>
  <div class="photo photo-hands" role="img" aria-label="Foto: mehrere Hände treffen sich zu einem Faustgruß"></div>

  <p class="intro-lead">Mit mehr als 15 Jahren Erfahrung in der Vermittlung von Fach- und Führungskräften, steht Ihnen das Team von klarweg-job.de als vertrauensvoller Partner bei Ihrem Jobwechsel zur Seite.</p>
  <ul class="benefits">
    <li><svg width="28" height="28" viewBox="0 0 28 28"><circle cx="14" cy="14" r="13" fill="#67bb46"/><path d="M8 14.5l4 4 8-8" stroke="#fff" stroke-width="2.6" fill="none" stroke-linecap="round" stroke-linejoin="round"/></svg><span>Mit mehr als 15 Jahren Erfahrung in der Vermittlung von Fach- und Führungskräften, steht Ihnen das Team von klarweg-job.de als vertrauensvoller Partner bei Ihrem Jobwechsel zur Seite.</span></li>
    <li><svg width="28" height="28" viewBox="0 0 28 28"><circle cx="14" cy="14" r="13" fill="#67bb46"/><path d="M8 14.5l4 4 8-8" stroke="#fff" stroke-width="2.6" fill="none" stroke-linecap="round" stroke-linejoin="round"/></svg><span>Gemeinsam finden wir die ideale Stelle, welche auf Grund Ihrer persönlichen Wünsche und Vorstellungen am besten zu Ihnen passt.</span></li>
    <li><svg width="28" height="28" viewBox="0 0 28 28"><circle cx="14" cy="14" r="13" fill="#67bb46"/><path d="M8 14.5l4 4 8-8" stroke="#fff" stroke-width="2.6" fill="none" stroke-linecap="round" stroke-linejoin="round"/></svg><span>Lehnen Sie sich bequem zurück und überlassen das Finden Ihres neuen Arbeitsplatzes uns.</span></li>
    <li><svg width="28" height="28" viewBox="0 0 28 28"><circle cx="14" cy="14" r="13" fill="#67bb46"/><path d="M8 14.5l4 4 8-8" stroke="#fff" stroke-width="2.6" fill="none" stroke-linecap="round" stroke-linejoin="round"/></svg><span>Am Ende des Tage entscheiden Sie, ob ein Vorstellungsgespräch stattfinden soll oder wir für Sie weitersuchen!</span></li>
  </ul>

  <div class="photo photo-team" role="img" aria-label="Foto: jubelnde Gruppe junger Menschen in einem hellen Büro"></div>
  <p class="kicker">KONTAKT</p>
  <h2 class="contact-title">Wir freuen uns auf dich</h2>

  <div class="field f-first">Vorname*</div>
  <div class="field f-last">Nachname*</div>
  <div class="field f-mail">E-Mail*</div>
  <div class="field f-call filled">Rückruf erwünscht?<svg width="24" height="14" viewBox="0 0 24 14"><path d="M2 2l10 10 10-10" stroke="#333" stroke-width="2.4" fill="none"/></svg></div>
  <div class="field f-cv filled">Lebenslauf hochladen<svg width="22" height="22" viewBox="0 0 22 22" fill="none" stroke="#333" stroke-width="1.6"><circle cx="3" cy="4" r="1.3"/><circle cx="3" cy="11" r="1.3"/><circle cx="3" cy="18" r="1.3"/><rect x="7" y="2" width="13" height="4" rx="2"/><rect x="7" y="9" width="13" height="4" rx="2"/><rect x="7" y="16" width="13" height="4" rx="2"/></svg></div>
  <div class="field f-msg">Nachricht</div>
  <div class="send">Absenden<svg width="26" height="20" viewBox="0 0 26 20" fill="none" stroke="#fff" stroke-width="2"><rect x="1.5" y="1.5" width="23" height="17" rx="3"/><path d="M2 3l11 8 11-8"/></svg></div>

  <footer class="footer">
    <div class="brand"><span class="brand-mark"></span>KLARWEG JOB</div>
    <nav class="footer-nav"><a href="#">Home</a><a href="#">Bewerber über uns</a><a href="#">Wir über uns</a></nav>
    <div class="social"><span></span><span></span></div>
    <div class="footer-rule"></div>
    <p class="copyright">© 2024 farbwandel-media.com</p>
    <div class="legal"><span>Impressum</span><span>Datenschutz</span></div>
  </footer>
</div>
</body>
</html>
```